Redesign My Travel Voucher Coupons-Please redesign the flyers I have attached to this brief.

These designs will be catered towards like travel agency vacation stays...luxury resort stays, hotel and airfare getaways, etc. so must have a travel theme but more importantly professional trustworthy appeal...

Please redesign the flyers I have attached to this brief.

I have attached my existing designs. Please use all existing content and elements exactly but make the design much better...also, please keep in mind that these would be full color and printer friendly...

Target Market(s)

Consumers. People receive these vouchers from businesses that run marketing promotions and contests and giveaways. So the look and feel must feel professional and trustworthy but not cheesy and fake.

Industry/Entity Type

Hotel

Requirements
Must have
• Please use all existing content and elements exactly but make the design much better...also, please keep in mind that these would be full color and printer friendly...

MUST HAVE ALL EXISTING CONTENT EXACT NO EXCEPTIONS
Nice to have
• These designs will be catered towards like travel agency vacation stays...luxury resort stays, hotel and airfare getaways, etc. so must have a travel theme but more importantly professional trustworthy appeal...

Should not have

```html
<!DOCTYPE html>
<html lang="en">
<head>
<meta charset="utf-8">
<title>2 Night Hotel Stay Certificate</title>
<link href="https://fonts.googleapis.com/css2?family=Oswald:wght@200;300;500;600&family=Roboto:wght@400;500;700;900&display=swap" rel="stylesheet">
<style>
  :root{
    --mat:#000000;
    --red:#d1202f;
    --red-dark:#a8151f;
    --ink:#1e1e1e;
    --body:#333333;
    --icon:#5a5a5a;
    --paper:#f4f4f4;
    --silver:#9a9a9a;
  }
  *{margin:0;padding:0;box-sizing:border-box}
  html,body{width:974px;height:1200px;overflow:hidden;background:var(--mat)}
  body{position:relative;font-family:"Roboto",Arial,sans-serif;color:var(--body)}
  .flyer{position:absolute;left:92px;top:89px;width:790px;height:1022px;overflow:hidden;
    background:linear-gradient(180deg,#ffffff 0%,var(--paper) 45%,#e9e9e9 80%,#f7f7f7 100%)}
  .hero{position:absolute;left:0;top:0;width:790px;height:480px}
  .headline{position:absolute;left:27px;top:18px}
  .enjoy{position:absolute;left:0;top:0;font-family:"Oswald",sans-serif;font-weight:500;font-size:128px;line-height:1;color:var(--red);letter-spacing:-2px;white-space:nowrap}
  .nights{position:absolute;left:234px;top:70px;font-family:"Oswald",sans-serif;font-weight:200;font-size:44px;line-height:1;color:var(--ink);white-space:nowrap}
  .stay-band{position:absolute;left:0;top:111px;width:406px;height:50px}
  .stay-band svg{position:absolute;inset:0}
  .stay-band span{position:absolute;left:8px;top:0;font-family:"Roboto",sans-serif;font-weight:900;font-size:47px;line-height:50px;color:#fff;letter-spacing:.5px}
  .sub-red{position:absolute;left:27px;top:181px;font-weight:900;font-size:23.5px;color:var(--red);white-space:nowrap}
  .sub-dark{position:absolute;left:27px;top:209px;font-weight:900;font-size:17.5px;line-height:21px;color:var(--ink);white-space:nowrap}
  .sponsor{position:absolute;left:598px;top:1px;width:157px;height:120px;background:#fff;text-align:center;padding-top:27px}
  .sponsor .lead{font-weight:700;font-size:9px;color:var(--red)}
  .sponsor .brand{margin:9px auto 6px;display:flex;align-items:center;justify-content:center;gap:4px;font-weight:700;font-size:7.5px;color:#1f6fc4;line-height:1.05;text-align:left}
  .sponsor .brand i{width:9px;height:9px;border-radius:50%;background:#1f6fc4;display:block}
  .sponsor .person{font-size:11.5px;color:#333;line-height:13.5px}
  .sponsor .web{font-size:8.6px;color:#333;margin-top:1px}
  .photo-circle{position:absolute;border-radius:50%}
  .tag{position:absolute;height:24px;color:#fff;font-family:"Oswald",sans-serif;font-weight:500;font-size:17px;line-height:24px;padding-left:9px}
  .tag svg{position:absolute;left:0;top:0;z-index:0}
  .tag span{position:relative;z-index:1}
  .copy{position:absolute;font-size:10px;line-height:12.2px;text-align:justify;color:var(--body)}
  .feature{position:absolute;display:flex;align-items:flex-start;gap:0}
  .feature svg{position:absolute;left:0;top:0}
  .feature p{position:absolute;font-size:12px;line-height:15px;color:var(--ink);white-space:nowrap}
  .divider{position:absolute;left:361px;top:486px;width:1px;height:399px;background:#8a8a8a}
  .quote{position:absolute;left:393px;top:823px;width:355px;font-size:10px;line-height:12.2px;color:var(--body)}
  .qmark{position:absolute;font-family:"Oswald",sans-serif;font-weight:600;font-size:30px;color:#666;line-height:1}
  .author{position:absolute;right:46px;top:876px;font-size:10px;color:var(--body)}
  .redeem{position:absolute;left:29px;top:901px;width:732px;height:93px;border:2px dashed var(--red);border-radius:12px}
  .redeem .split{position:absolute;left:182px;top:4px;bottom:4px;border-left:2px dashed var(--red)}
  .cert{position:absolute;left:0;top:0;width:182px;text-align:center}
  .cert .label{font-size:11px;color:#222;margin-top:11px}
  .cert .value{font-size:17px;color:var(--red);line-height:20px}
  .cert hr{width:58%;margin:4px auto 5px;border:0;border-top:1px solid #888}
  .offer{position:absolute;left:184px;right:0;top:0;text-align:center}
  .offer .cta{font-size:14.5px;line-height:18px;color:#222;margin-top:9px}
  .offer .url{font-size:21px;letter-spacing:3.2px;color:var(--red);margin-top:4px;font-weight:500}
  .offer .terms{font-size:8px;color:#222;margin-top:3px}
</style>
</head>
<body>
<main class="flyer">

  <svg class="hero" viewBox="0 0 790 480" aria-hidden="false">
    <defs>
      <linearGradient id="lounge" x1="0" y1="0" x2="1" y2="0">
        <stop offset="0" stop-color="#c9c2b8"/>
        <stop offset=".45" stop-color="#b9aea3"/>
        <stop offset=".7" stop-color="#8a6a4f"/>
        <stop offset="1" stop-color="#5b4030"/>
      </linearGradient>
      <linearGradient id="swoosh" x1="0" y1="0" x2="1" y2="0">
        <stop offset="0" stop-color="#bdbdbd"/>
        <stop offset=".5" stop-color="#6f6f6f"/>
        <stop offset="1" stop-color="#a9a9a9"/>
      </linearGradient>
    </defs>
    <path d="M0 380 C60 430 140 470 240 468 C360 466 440 430 500 370 C545 325 580 300 630 300 C690 300 730 360 790 402 L790 418 C730 380 690 322 630 322 C585 322 550 345 505 392 C445 455 360 484 240 484 C140 484 60 455 0 405 Z" fill="url(#swoosh)"/>
    <path role="img" aria-label="Photo of an upscale hotel lounge with sofas, a pool table and warm wood panelling" d="M0 0 H790 V398 C735 360 695 296 630 290 C575 286 540 318 495 365 C440 422 360 455 240 456 C140 457 60 420 0 372 Z" fill="url(#lounge)"/>
  </svg>

  <div class="headline">
    <div class="enjoy">ENJOY</div>
    <div class="nights">A 2 NIGHT</div>
    <div class="stay-band">
      <svg width="406" height="50" viewBox="0 0 406 50"><path d="M0 0 H356 L406 50 H0 Z" fill="var(--red)"/></svg>
      <span>HOTEL STAY</span>
    </div>
  </div>
  <div class="sub-red">of 3+ Star Hotel Accommodations</div>
  <div class="sub-dark">In The City Of Your Choice Of Over 50 Of<br>The Most Popular Destinations Available!</div>

  <aside class="sponsor">
    <div class="lead">Compliments Of</div>
    <div class="brand"><i></i><span>NORTHPOINT<br>REWARD PARTNERS</span></div>
    <div class="person">Dana Whitfield<br>555-204-3190</div>
    <div class="web">www.GrowYourClientBase.com</div>
  </aside>

  <div class="photo-circle" role="img" aria-label="Photo of a hotel receptionist handing over a key card" style="left:470px;top:295px;width:196px;height:196px;background:radial-gradient(circle,#e6e0d8 0%,#b8b0a6 70%);box-shadow:0 0 0 6px #d7d7d7,0 0 0 8px #8d8d8d"></div>
  <div class="photo-circle" role="img" aria-label="Photo of a hotel room door opening onto a bed" style="left:433px;top:483px;width:142px;height:142px;background:linear-gradient(90deg,#eef1f3 0%,#dfe4e8 55%,#b98f6a 70%,#a57c58 100%);box-shadow:0 0 0 5px #d9d9d9,0 0 0 7px #8f8f8f"></div>
  <div class="photo-circle" role="img" aria-label="Photo of a resort pool surrounded by palm trees" style="left:590px;top:467px;width:158px;height:158px;background:linear-gradient(180deg,#a9d3ef 0%,#c8e2f0 30%,#5f8a4f 50%,#3fb7dc 70%,#8ca66b 100%);box-shadow:0 0 0 5px #d9d9d9,0 0 0 7px #8f8f8f"></div>

  <div class="tag" style="left:27px;top:486px;width:160px">
    <svg width="160" height="24"><path d="M0 0 H138 L160 24 H0 Z" fill="var(--red)"/></svg><span>EXCLUSIVELY FOR:</span>
  </div>
  <p class="copy" style="left:38px;top:516px;width:305px">There is no doubt that everyone wishes they can take a much needed vacation to just relax and unwind while having fun at the same time! Enjoy two nights of hotel accommodations in the city of your choice of over 50 of the hottest, most desired vacation spots around the country. Thanks to the business you received this certificate from, now you can enjoy a nice little mini vacation you deserve!</p>

  <div class="tag" style="left:27px;top:621px;width:160px">
    <svg width="160" height="24"><path d="M0 0 H138 L160 24 H0 Z" fill="var(--red)"/></svg><span>FEATURES</span>
  </div>

  <div class="feature" style="left:29px;top:655px">
    <svg width="36" height="36" viewBox="0 0 36 36"><circle cx="19" cy="17" r="16" fill="var(--icon)"/><path d="M10 20 L28 12 L29 14 L20 19 L23 26 L21 26 L16 21 L12 23 Z" fill="#fff"/><circle cx="6" cy="30" r="5" fill="#fff" stroke="var(--icon)" stroke-width="1.5"/></svg>
    <p style="left:43px;top:3px">Travel 7 Days<br>A Week</p>
  </div>
  <div class="feature" style="left:194px;top:655px">
    <svg width="32" height="36" viewBox="0 0 32 36"><g fill="var(--icon)"><circle cx="9" cy="5" r="4"/><circle cx="21" cy="5" r="4"/><rect x="4" y="10" width="10" height="14" rx="2"/><rect x="16" y="10" width="10" height="14" rx="2"/><circle cx="5" cy="22" r="3"/><circle cx="27" cy="22" r="3"/><rect x="2" y="26" width="6" height="9" rx="1"/><rect x="24" y="26" width="6" height="9" rx="1"/><rect x="6" y="24" width="3" height="11"/><rect x="21" y="24" width="3" height="11"/></g></svg>
    <p style="left:36px;top:3px">Good For Two Adults<br>&amp; Two Children</p>
  </div>

  <div class="feature" style="left:31px;top:716px">
    <svg width="32" height="34" viewBox="0 0 32 34"><rect x="2" y="5" width="28" height="27" rx="3" fill="none" stroke="var(--icon)" stroke-width="2.5"/><rect x="2" y="5" width="28" height="7" fill="var(--icon)"/><g fill="var(--icon)"><rect x="7" y="1" width="3" height="7"/><rect x="14" y="1" width="3" height="7"/><rect x="21" y="1" width="3" height="7"/><rect x="7" y="15" width="4" height="3"/><rect x="14" y="15" width="4" height="3"/><rect x="21" y="15" width="4" height="3"/><rect x="7" y="21" width="4" height="3"/><rect x="14" y="21" width="4" height="3"/><rect x="21" y="21" width="4" height="3"/></g></svg>
    <p style="left:41px;top:2px">Multiple Travel Date<br>Requests Allowed</p>
  </div>
  <div class="feature" style="left:196px;top:716px">
    <svg width="26" height="34" viewBox="0 0 26 34"><path d="M1 1 H18 L25 8 V33 H1 Z" fill="var(--icon)"/><g fill="#fff"><rect x="5" y="18" width="16" height="2"/><rect x="5" y="23" width="16" height="2"/><rect x="5" y="28" width="16" height="2"/></g><text x="5" y="14" font-size="11" font-weight="700" fill="#fff" font-family="Roboto,sans-serif">$</text></svg>
    <p style="left:34px;top:2px">Pay Just<br>The Taxes &amp; Fees</p>
  </div>

  <div class="feature" style="left:29px;top:778px">
    <svg width="34" height="34" viewBox="0 0 34 34"><circle cx="17" cy="17" r="16" fill="var(--icon)"/><circle cx="17" cy="17" r="9" fill="none" stroke="#fff" stroke-width="2"/><path d="M13 17 L16 20 L21 14" fill="none" stroke="#fff" stroke-width="2"/></svg>
    <p style="left:43px;top:-2px">No Timeshare No<br>Sales Presentation<br>Guaranteed!</p>
  </div>
  <div class="feature" style="left:186px;top:778px">
    <svg width="36" height="36" viewBox="0 0 36 36"><g fill="none" stroke="var(--icon)" stroke-width="2.2"><path d="M11 34 C4 25 2 21 2 17 A9 9 0 0 1 20 17 C20 21 18 25 11 34 Z"/><circle cx="11" cy="17" r="3"/><path d="M29 15 C25 10 24 8 24 6 A5 5 0 0 1 34 6 C34 8 33 10 29 15 Z"/></g><g fill="var(--icon)"><circle cx="22" cy="24" r="2"/><circle cx="27" cy="24" r="2"/><circle cx="23" cy="30" r="2"/></g></svg>
    <p style="left:44px;top:-2px">Your Choice Of<br>Over 50 Luxury<br>Destinations</p>
  </div>

  <div class="feature" style="left:28px;top:848px">
    <svg width="34" height="36" viewBox="0 0 34 36"><g fill="none" stroke="var(--icon)" stroke-width="1.8"><path d="M6 8 H28 M22 3 L28 8 L22 13"/><path d="M28 30 H6 M12 25 L6 30 L12 35"/><circle cx="9" cy="19" r="6"/><circle cx="25" cy="19" r="6"/></g></svg>
    <p style="left:44px;top:3px">Fully Transferable<br>To Another Person</p>
  </div>
  <div class="feature" style="left:195px;top:848px">
    <svg width="30" height="32" viewBox="0 0 30 32"><rect x="1" y="4" width="28" height="27" rx="3" fill="var(--icon)"/><g fill="var(--icon)"><rect x="5" y="0" width="3" height="6"/><rect x="13" y="0" width="3" height="6"/><rect x="21" y="0" width="3" height="6"/></g><rect x="3" y="9" width="24" height="1.5" fill="#fff"/><path d="M8 22 L22 16 L23 18 L16 21 L18 26 L16 26 L13 22 L10 24 Z" fill="#fff"/></svg>
    <p style="left:35px;top:3px">24 Months To<br>Complete Travel<br>After Redemption</p>
  </div>

  <div class="divider"></div>

  <div class="tag" style="left:375px;top:638px;width:182px">
    <svg width="182" height="24"><path d="M0 0 H160 L182 24 H0 Z" fill="var(--red)"/></svg><span>HOW CAN WE DO THIS?</span>
  </div>
  <p class="copy" style="left:384px;top:666px;width:378px">We contract with the world leading hotel chains and resorts to help them fill their otherwise empty rooms. We help fill empty rooms which the hotels, resorts and cruise lines turn into additional revenue from other areas of their property and future bookings.<br>Hotels rarely experience full occupancy, yet they remain open, providing rooms and services at fixed costs. So when hotels give out their rooms by partnering with marketing companies like us, they might miss out on the room fee, but they already didn't have that in the first place, at least now they have the opportunity to gain a customer for their in-house restaurants, room service, their casinos, an extra day stay, future bookings, etc.</p>

  <div class="tag" style="left:375px;top:793px;width:157px">
    <svg width="157" height="24"><path d="M0 0 H135 L157 24 H0 Z" fill="var(--red)"/></svg><span>WHAT OTHERS SAY</span>
  </div>
  <span class="qmark" style="left:374px;top:818px">&ldquo;</span>
  <p class="quote">Being able to stay right on the strip in Las Vegas was great. I love that we were able to walk around to all the sites and attractions. The fountains at the Belmonte were AMAZING! The Gondola ride at the Veranda was very nice. I LOVED the atmosphere and the food. The whole experience was awesome. THANK YOU!</p>
  <span class="qmark" style="left:459px;top:868px">&rdquo;</span>
  <p class="author">Marissa T. Fresno, CA</p>

  <section class="redeem">
    <div class="cert">
      <p class="label">Certificate ID</p>
      <p class="value">107083-11266</p>
      <hr>
      <p class="label" style="margin-top:0">Expires</p>
      <p class="value">11/07/2020</p>
    </div>
    <div class="split"></div>
    <div class="offer">
      <p class="cta">VIEW ALL THE DETAILS OF THIS SPECIAL OFFER<br>AND REDEEM ONLINE AT</p>
      <p class="url">WWW.GETAWAYVOUCHERDESK.COM</p>
      <p class="terms">*Terms and Conditions apply see website for details</p>
    </div>
  </section>

</main>
</body>
</html>
```